Mara Joss Advisory Business Cards

Hi - using the information and logo provided I require a two sided business card designed with the following information. The business card is a 'mini card' 3.5" x 1.25".

Front of card should be the logo attached but inverted (so the background is the peach colour and the logo white).

Back should have these details. If we can't fit the Instragram and Facebook part can we just put the little logos.

Ruth Penderby

Art and Design Consultant
Dealer - Curator - Events - Styling - Creative Sourcing

P: 0462 913 058
E: ruth@marajossadvisory.example
W: www.marajossadvisory.example
I (instagram image please): marajossadvisory F (Facebook image please): MaraJossAdvisor

Target Market(s)

Galleries, artists, art buyers, interior design clients, event managers, creative types

Industry/Entity Type

Business

```html
<!DOCTYPE html>
<html lang="en">
<head>
<meta charset="utf-8">
<title>Mara Joss Advisory – Business Cards</title>
<link rel="stylesheet" href="https://fonts.googleapis.com/css2?family=Questrial&display=swap">
<style>
  :root {
    --backdrop: #e6e6e6;
    --peach: #f0b89c;
    --white: #ffffff;
    --charcoal: #55565a;
    --text-dark: #4a4a4d;
  }
  * { margin: 0; padding: 0; box-sizing: border-box; }
  html, body {
    width: 1200px;
    height: 900px;
    overflow: hidden;
    background: var(--backdrop);
    font-family: "Questrial", "Century Gothic", sans-serif;
  }
  .canvas { position: relative; width: 1200px; height: 900px; }
  .card {
    position: absolute;
    left: 54px;
    width: 1093px;
    height: 390px;
    overflow: hidden;
  }
  .card--details { top: 39px; background: var(--white); }
  .card--brand { top: 473px; background: var(--peach); }

  .card__shapes { position: absolute; inset: 0; }

  .details { position: absolute; left: 19px; top: 0; color: var(--text-dark); }
  .details__name {
    position: absolute; top: 24px; white-space: nowrap;
    font-size: 33px; color: var(--white); font-weight: 400;
  }
  .details__role {
    position: absolute; top: 68px; white-space: nowrap;
    font-size: 22px; color: var(--text-dark);
  }
  .details__services {
    position: absolute; top: 97px; white-space: nowrap;
    font-size: 20px; color: var(--white);
  }
  .contact-list, .social-list { list-style: none; position: absolute; left: 0; }
  .contact-list { top: 174px; }
  .social-list { top: 302px; }
  .contact-list li, .social-list li {
    display: flex; align-items: center; white-space: nowrap;
  }
  .contact-list li { height: 35px; font-size: 26px; }
  .social-list li { height: 31px; font-size: 23px; }
  .contact-icon { width: 26px; height: 26px; margin-right: 9px; flex: none; }
  .social-square {
    width: 18px; height: 18px; margin: 0 12px 0 3px; flex: none;
    background: var(--white);
  }

  .brand-lockup {
    position: absolute; left: 660px; top: 0; width: 420px; height: 390px;
    display: flex; flex-direction: column; align-items: center; justify-content: center;
  }
  .brand-lockup__circle {
    width: 140px; height: 140px; border-radius: 50%;
    border: 6px solid var(--peach); margin-bottom: 26px;
  }
  .brand-lockup__name {
    font-size: 40px; line-height: 1.15; letter-spacing: 5px;
    text-transform: uppercase; text-align: center; color: var(--charcoal);
  }

  .brand-mark {
    position: absolute; inset: 0;
    display: flex; align-items: center; justify-content: center;
  }
  .brand-mark__name {
    font-size: 46px; letter-spacing: 8px; text-transform: uppercase;
    color: var(--white); white-space: nowrap;
  }
</style>
</head>
<body>
<main class="canvas">

  <section class="card card--details" aria-label="Card back with contact details">
    <svg class="card__shapes" viewBox="0 0 1093 390" width="1093" height="390" aria-hidden="true">
      <path d="M0 0 H606 C588 120 612 290 714 390 H0 Z" fill="var(--peach)"/>
      <path d="M614 0 H704 C652 60 626 190 640 300 C612 220 604 100 614 0 Z" fill="var(--charcoal)"/>
    </svg>

    <div class="details">
      <h1 class="details__name">Ruth Penderby</h1>
      <p class="details__role">Art and Design Consultant</p>
      <p class="details__services">Dealer - Curator - Events - Styling - Creative Sourcing</p>

      <ul class="contact-list">
        <li>
          <svg class="contact-icon" viewBox="0 0 24 24" aria-hidden="true">
            <path fill="var(--white)" d="M6.6 10.8a15.1 15.1 0 0 0 6.6 6.6l2.2-2.2a1 1 0 0 1 1-.25 11.4 11.4 0 0 0 3.6.6 1 1 0 0 1 1 1V20a1 1 0 0 1-1 1A17 17 0 0 1 3 4a1 1 0 0 1 1-1h3.5a1 1 0 0 1 1 1c0 1.25.2 2.45.6 3.6a1 1 0 0 1-.25 1z"/>
          </svg>
          0462 913 058
        </li>
        <li>
          <svg class="contact-icon" viewBox="0 0 24 24" aria-hidden="true">
            <g fill="none" stroke="var(--white)" stroke-width="1.6">
              <circle cx="12" cy="12" r="9.5"/>
              <ellipse cx="12" cy="12" rx="4.2" ry="9.5"/>
              <path d="M2.5 12h19M4 7h16M4 17h16"/>
            </g>
          </svg>
          www.marajossadvisory.example
        </li>
        <li>
          <svg class="contact-icon" viewBox="0 0 24 24" aria-hidden="true">
            <g fill="none" stroke="var(--white)" stroke-width="1.6">
              <rect x="2" y="5" width="20" height="14"/>
              <path d="M2 5l10 8 10-8M2 19l7-6M22 19l-7-6"/>
            </g>
          </svg>
          ruth@marajossadvisory.example
        </li>
      </ul>

      <ul class="social-list">
        <li><span class="social-square" aria-hidden="true"></span>marajossadvisory</li>
        <li><span class="social-square" aria-hidden="true"></span>MaraJossAdvisor</li>
      </ul>
    </div>

    <div class="brand-lockup">
      <span class="brand-lockup__circle" aria-hidden="true"></span>
      <p class="brand-lockup__name">Mara Joss<br>Advisory</p>
    </div>
  </section>

  <section class="card card--brand" aria-label="Card front with brand name">
    <div class="brand-mark">
      <p class="brand-mark__name">Mara Joss Advisory</p>
    </div>
  </section>

</main>
</body>
</html>
```